Lantern Ridge Fund Wordpress Template
Lantern Ridge Fund
Lantern Ridge Fund Wordpress Template - Financial Services
Creative Brief
Forex Trading Company
Financial Services
Corporate, small, medium and large Investors
The Site should include the following buttons:
Home - About us - Introduction - The Forex Market - Investment - Contact us - Disclaimer
The Website should be in a modern style and in the colors of the Logo. I don't like Standard sites, I prefer the special BAAAAM effect when you enter a website, nice backround, great color combination, modern but not to playful as it has to be serious as well.
BrookMill BrookMill
To Sandalwick: Thanks for the Draft. The Layout is ok, a bit too much text in the middle and also here I would choose a more Forex/Currency related picture. Thx!
To oakandkettle: Thanks for the Draft. It's a nice design and a good start. Could you delete the "Financial Services" on in the middle of the page and maybe take a more Forex related picture as main picture, something Forex/Currency related. Thanks!
oakandkettle oakandkettle
thanks for the feedback, expecting your comments, so that I can do the changes

```html
<!DOCTYPE html>
<html lang="en">
<head>
<meta charset="utf-8">
<title>Lantern Ridge Fund</title>
<link rel="stylesheet" href="https://fonts.googleapis.com/css2?family=Arimo:ital,wght@0,400;0,700;1,400&family=Russo+One&family=Lilita+One&family=Kalam&display=swap">
<style>
  :root {
    --navy: #1f2f4f;
    --blue: #3a86c8;
    --ink: #222a33;
    --muted: #555d66;
    --page: #e4e6e9;
    --panel: #ffffff;
    --quote-bg: #d6e4ee;
    --band: #2b3548;
    --footer: #7b7c82;
    --footer-dark: #3c3e44;
  }
  * { box-sizing: border-box; margin: 0; padding: 0; }
  html, body { width: 1200px; height: 799px; overflow: hidden; }
  body {
    position: relative;
    font-family: "Arimo", Arial, sans-serif;
    color: var(--ink);
    background: linear-gradient(180deg, #f4f5f6 0, #e9ebee 92px, #cfd6dc 200px, #e5e8eb 378px, var(--page) 665px);
  }
  .site-header {
    position: absolute; left: 0; top: 0; width: 1200px; height: 92px;
    background: #fbfbfb;
  }
  .brand {
    position: absolute; left: 218px; top: 28px;
    display: flex; align-items: center; gap: 10px;
    font-family: "Arimo", Arial, sans-serif; font-weight: 700;
    font-size: 24px; color: var(--navy);
  }
  .brand-mark { width: 30px; height: 30px; background: var(--navy); }
  .main-nav {
    position: absolute; left: 508px; top: 20px; width: 480px; height: 50px;
    display: flex; justify-content: space-between; align-items: center;
    list-style: none; font-size: 12.5px; color: var(--ink);
  }
  .main-nav li { text-align: center; line-height: 14px; }
  .hero {
    position: absolute; left: 212px; top: 92px; width: 776px; height: 286px;
    border-top: 3px solid #9dc4e2;
  }
  .hero-photo { position: absolute; inset: 0; width: 100%; height: 100%; }
  .hero-title {
    position: absolute; left: 44px; top: 38px;
    font-family: "Russo One", sans-serif; font-size: 50px; letter-spacing: 2px;
    color: #2e2f33; text-shadow: 2px 2px 0 #ffffff, 4px 4px 3px rgba(0,0,0,.35);
  }
  .hero-lead {
    position: absolute; left: 106px; top: 104px;
    font-size: 33px; line-height: 41px; color: #2f3338;
  }
  .content {
    position: absolute; left: 218px; top: 378px; width: 770px; height: 287px;
    display: flex;
  }
  .welcome {
    width: 454px; background: var(--panel);
    border: 4px solid #d9dcdf; border-top: 0; padding: 30px 24px 0 24px;
  }
  .welcome h1 {
    font-family: "Lilita One", sans-serif; font-weight: 400; font-size: 19px;
    color: var(--ink); margin-bottom: 22px;
  }
  .welcome h1 .accent { color: var(--blue); }
  .welcome p { font-size: 10.5px; line-height: 12px; color: var(--muted); margin-bottom: 18px; width: 400px; }
  .read-more { font-size: 13px; color: var(--ink); text-decoration: underline; }
  .welcome .read-more { position: absolute; left: 28px; top: 248px; }
  .testimonial {
    position: relative; width: 176px; background: var(--quote-bg); padding: 20px 14px 0 14px;
  }
  .testimonial .mark { font-family: Georgia, serif; font-size: 26px; color: var(--ink); line-height: 16px; }
  .testimonial blockquote {
    font-family: "Kalam", cursive; font-size: 11.5px; line-height: 14px; color: var(--ink);
    margin-top: 10px;
  }
  .testimonial .read-more { position: absolute; left: 14px; top: 226px; }
  .testimonial .posted { position: absolute; left: 14px; top: 256px; font-size: 11.5px; color: var(--ink); }
  .client-photo { width: 140px; height: 287px; display: block; }
  .band { position: absolute; left: 0; top: 665px; width: 1200px; height: 13px; background: var(--band); }
  .site-footer {
    position: absolute; left: 0; top: 678px; width: 1200px; height: 121px;
    background: linear-gradient(180deg, #6e6f75, var(--footer) 40%, #8a8b90);
  }
  .social { position: absolute; left: 465px; top: 36px; display: flex; gap: 6px; list-style: none; }
  .social li { width: 28px; height: 28px; border-radius: 50%; background: #54565c; border: 2px solid #3f4147; }
  .copyright {
    position: absolute; left: 0; bottom: 0; width: 1200px; height: 27px;
    background: var(--footer-dark); color: #ffffff; font-size: 11px;
    display: flex; align-items: center; justify-content: center;
  }
</style>
</head>
<body>
  <header class="site-header">
    <div class="brand"><span class="brand-mark"></span>Lantern Ridge Fund</div>
    <ul class="main-nav">
      <li>Home</li>
      <li>About Us</li>
      <li>Introduction</li>
      <li>The<br>Forex<br>Market</li>
      <li>Investment</li>
      <li>Contact Us</li>
      <li>Disclaimer</li>
    </ul>
  </header>

  <section class="hero">
    <svg class="hero-photo" viewBox="0 0 776 286" preserveAspectRatio="none" role="img" aria-label="Photo of a smiling businesswoman in a bright modern office hallway">
      <defs>
        <linearGradient id="heroTone" x1="0" y1="0" x2="1" y2="0">
          <stop offset="0" stop-color="#e6ebef"/>
          <stop offset="0.55" stop-color="#d3dce3"/>
          <stop offset="0.8" stop-color="#c2ccd4"/>
          <stop offset="1" stop-color="#e8ecef"/>
        </linearGradient>
      </defs>
      <rect width="776" height="286" fill="url(#heroTone)"/>
      <rect x="540" y="40" width="180" height="246" fill="#b9bec4" opacity="0.45"/>
    </svg>
    <div class="hero-title">GET READY..!</div>
    <p class="hero-lead">You Are Going<br>To Have A Better<br>Financial Status</p>
  </section>

  <main class="content">
    <section class="welcome">
      <h1><span class="accent">Welcome To</span> Lantern Ridge Fund</h1>
      <p>Lorem ipsum dolor sit amet, consectetur adipiscing elit. Nullam sit amet metus lorem, non vestibulum metus. Integer condimentum est quis leo fermentum sit amet rhoncus lorem dignissim. Aenean ornare rhoncus commodo. Maecenas turpis purus, ultrices in tristique eget, dapibus velit. Proin tortor nibh, tristique at ultrices ultrices, porttitor . Sed fermentum tellus ac sapien vulputate pellentesque.</p>
      <p>Lorem ipsum dolor sit amet, consectetur adipiscing elit. Nullam sit amet metus lorem, non vestibulum metus. Integer condimentum est quis leo fermentum sit amet rhoncus lorem dignissim.</p>
      <span class="read-more">Read More...</span>
    </section>
    <aside class="testimonial">
      <div class="mark">&ldquo;</div>
      <blockquote>Lorem ipsum dolor sit amet, consectetur adipiscing elit. Nullam sit amet metus lorem, non vestibulum metus. Integer. Lorem ipsum dolor sit amet, consectetur adipiscing elit. Nullam sit......</blockquote>
      <span class="read-more">Read More...</span>
      <span class="posted">Posted On 31st May 2013</span>
    </aside>
    <svg class="client-photo" viewBox="0 0 140 287" preserveAspectRatio="none" role="img" aria-label="Portrait photo of a smiling client in a shirt">
      <defs>
        <linearGradient id="clientTone" x1="0" y1="0" x2="0" y2="1">
          <stop offset="0" stop-color="#e9ecee"/>
          <stop offset="0.5" stop-color="#b9a594"/>
          <stop offset="1" stop-color="#7f95a3"/>
        </linearGradient>
      </defs>
      <rect width="140" height="287" fill="url(#clientTone)"/>
    </svg>
  </main>

  <div class="band"></div>

  <footer class="site-footer">
    <ul class="social">
      <li></li><li></li><li></li><li></li><li></li><li></li><li></li><li></li>
    </ul>
    <div class="copyright">© 2013 | All Rights Reserved</div>
  </footer>
</body>
</html>
```